Calvanta Group Real Estate Company business cards

New business card design, we are generally happy with the basic layout of the existing front of business card, (feel free to change) but require a head shot photo on the back side.

http://www.calvanta.com.au/

Attached logos, and existing business card

------------------------------

Target Market(s)

Real estate

Industry/Entity Type

Real Estate

Contact Information for Business Card

Standard size double sided

Font styles to use
Other font styles liked:
• Futura

Requirements
Must have
• Photo head shot on the back side
Nice to have
• yes
Should not have
• No

```html
<!DOCTYPE html>
<html lang="en">
<head>
<meta charset="utf-8">
<title>Calvanta Group – Business Cards</title>
<link rel="stylesheet" href="https://fonts.googleapis.com/css2?family=Jost:wght@400;500&display=swap">
<style>
  :root {
    --purple: #4a3d78;
    --purple-deep: #3c3166;
    --orange: #e8962a;
    --paper: #f7f7f8;
    --grey-text: #8a8a94;
    --backdrop: #e9e6e1;
  }
  * { margin: 0; padding: 0; box-sizing: border-box; }
  html, body { width: 1200px; height: 864px; overflow: hidden; }
  body {
    background: var(--backdrop);
    font-family: "Jost", "Futura", sans-serif;
    position: relative;
  }
  .card {
    position: absolute;
    top: 273px;
    width: 520px;
    height: 318px;
    background: var(--paper);
    box-shadow: 0 10px 28px rgba(0,0,0,.18);
    overflow: hidden;
  }
  .card--front { left: 60px; }
  .card--back { left: 620px; }
  .card svg { position: absolute; inset: 0; }

  .wordmark {
    position: absolute;
    color: var(--purple);
    font-weight: 500;
    line-height: 1;
    letter-spacing: 0.5px;
  }
  .wordmark__sub {
    display: block;
    text-align: right;
    font-size: 10px;
    letter-spacing: 7px;
    margin-top: 2px;
  }
  .card--front .wordmark { left: 120px; top: 42px; font-size: 76px; }
  .card--front .wordmark__sub { font-size: 12px; letter-spacing: 9px; }
  .card--back .wordmark { right: 26px; bottom: 30px; font-size: 50px; }

  .contact-person {
    position: absolute;
    left: 32px;
    top: 228px;
    color: #fff;
  }
  .contact-person__name { font-size: 22px; font-weight: 500; }
  .contact-person__role,
  .contact-person__abn { font-size: 13px; line-height: 1.3; }

  .divider {
    position: absolute;
    left: 230px;
    top: 232px;
    width: 1px;
    height: 58px;
    background: rgba(255,255,255,.85);
  }
  .contact-list {
    position: absolute;
    left: 248px;
    top: 240px;
    list-style: none;
    color: #fff;
    font-size: 13px;
    line-height: 1.45;
  }
  .contact-list li { display: flex; align-items: center; gap: 7px; }
  .contact-list svg { position: static; width: 11px; height: 11px; flex: none; }

  .headshot-area { fill: url(#headshotTone); }
</style>
</head>
<body>

<section class="card card--front" aria-label="Business card front">
  <svg viewBox="0 0 520 318" width="520" height="318" aria-hidden="true">
    <defs>
      <linearGradient id="bandTone" x1="0" y1="0" x2="1" y2="1">
        <stop offset="0" stop-color="#564887"/>
        <stop offset="1" stop-color="#3a2f63"/>
      </linearGradient>
    </defs>
    <path d="M0,176 Q260,200 520,262 L520,318 L0,318 Z" fill="url(#bandTone)"/>
    <path d="M0,160 Q260,186 520,248" fill="none" stroke="var(--orange)" stroke-width="4"/>
  </svg>

  <div class="wordmark">calvanta<span class="wordmark__sub">GROUP</span></div>

  <div class="contact-person">
    <div class="contact-person__name">Daniel Tran</div>
    <div class="contact-person__role">Director</div>
    <div class="contact-person__abn">ABN: 12 345 678 901</div>
  </div>

  <div class="divider"></div>

  <ul class="contact-list">
    <li>
      <svg viewBox="0 0 12 12"><rect x="0" y="0" width="12" height="12" rx="2" fill="#fff"/><path d="M3,3.5 Q3,2.5 4,2.5 L8,2.5 Q9,2.5 9,3.5 L9,5 L7.5,5 L7,4 L5,4 L4.5,5 L3,5 Z M3.5,6 L8.5,6 L9,9.5 L3,9.5 Z" fill="var(--purple)"/></svg>
      0400 555 218
    </li>
    <li>
      <svg viewBox="0 0 12 12"><rect x="0" y="0" width="12" height="12" rx="2" fill="#fff"/><circle cx="6" cy="6" r="3.6" fill="none" stroke="var(--purple)" stroke-width="1"/><path d="M2.4,6 H9.6 M6,2.4 Q4,6 6,9.6 M6,2.4 Q8,6 6,9.6" fill="none" stroke="var(--purple)" stroke-width=".8"/></svg>
      www.calvanta.com.au
    </li>
    <li>
      <svg viewBox="0 0 12 12"><rect x="0" y="0" width="12" height="12" rx="2" fill="#fff"/><rect x="2.5" y="3.5" width="7" height="5" fill="none" stroke="var(--purple)" stroke-width="1"/><path d="M2.5,3.5 L6,6.5 L9.5,3.5" fill="none" stroke="var(--purple)" stroke-width="1"/></svg>
      daniel.tran@calvanta.com.au
    </li>
  </ul>
</section>

<section class="card card--back" aria-label="Business card back">
  <svg viewBox="0 0 520 318" width="520" height="318">
    <defs>
      <linearGradient id="headshotTone" x1="0" y1="0" x2="0" y2="1">
        <stop offset="0" stop-color="#dfe0e3"/>
        <stop offset=".55" stop-color="#c9c9cf"/>
        <stop offset="1" stop-color="#3a4560"/>
      </linearGradient>
    </defs>
    <path class="headshot-area" role="img" aria-label="Head shot photo of the director in a suit and tie"
          d="M0,0 L282,0 C262,70 276,150 250,220 C234,262 200,296 172,318 L0,318 Z"/>
    <path d="M282,0 C262,70 276,150 250,220 C234,262 200,296 172,318" fill="none" stroke="var(--orange)" stroke-width="5"/>
  </svg>
  <div class="wordmark">calvanta<span class="wordmark__sub">GROUP</span></div>
</section>

</body>
</html>
```